Tourism Marketing needing sleek, clear design for business card & proposal documents.

***Company background***
"Quiet Harbour" is a company specializing in tourism marketing and project management. We do international wholesale, event management as well as ongoing representation of tourism and hospitality companies.

***Target market***
We cater to tourism companies and hotel professionals.

***Task***
We would like to get a single sided business card designed (but will still consider two sided, we are open to any ideas you may have). The layout for this card should be modern and elegant. Currently we do not have a logo, but we would like our business name in a really simple typography for the business card (similar to Moonrise Palace's logo - www.moonrisepalace-example.com.au).We are after a design that is clear, strong enough to be recognised as Quiet Harbour that does not require any fancy design. Another option is a simple play on QH (Quiet Harbour) or simply have Quiet Harbour featured elsewhere on card more as a brand/logo.

Feel free to submit different fonts if you feel you have any other fonts/designs that may be suitable for this card other than sans serifs. Should this project be successful, we will be considering several other projects for business proposal templates and eventually a website design.

The information that needs to go on the card are as follows:

Marta Holloway
Director
Quiet Harbour
Tourism Marketing & Representation
87 Wendover Parade
Fernleigh, Westvale, 3999 Australia
T +61 498203617 E marta@quietharbour-example.com.au

***Look and feel***
We'd like the business card design to express the following:
Modern, sleek, elegant, simple, discreet, quality, subtle, professional, creative, innovation

In terms of typography, we like something really simple and blocky (similar font to Moonrise Palace's logo - www.moonrisepalace-example.com.au)

***Colour scheme***
Shades of grey and dark teal

***Note***
Although our main target market are professionals, we would like the business card design to be versatile enough to be used outside of the tourism industry and need to appeal to different markets.

I do not have existing logo. Was hoping for a design that may be clear, strong enough not to require one. Other option is a simple play on QH (Quiet Harbour) or simply have Quiet Harbour featured elsewhere on card more as a brand/logo.

Marta Holloway
Director
Quiet Harbour Pty Ltd 
87 Wendover Parade
T +61 498203617  E  marta@quietharbour-example.com.au

Thank you for designs so far. Many have used a mauve colour which matches our company profile. This is not necessary, as that is just a draft and will be completely redesigned, so dont  feel you need to incorporate the mauve.

My colour preferences are for a white or grey background, and I like fonts in dark teals, grey or other sophisticated but modern colours. feel free to submit different fonts if you you have other fonts you thing would be suitable for this card, along with sans serifs. Should this project be successful, we will be considering several others for business proposal templates and eventually website. 

Target Market(s)

International Hospitality Senior Executives, Directors of International Tourism Companies, Directors of Tourism Bodies Internationally, local Tourism

Industry/Entity Type

Hospitality

Requirements
Should not have
• must not have bright garish colour, swirly patterns or anything that dates too much.

```html
<!DOCTYPE html>
<html lang="en">
<head>
<meta charset="utf-8">
<title>Quiet Harbour – Business Card</title>
<link rel="stylesheet" href="https://fonts.googleapis.com/css2?family=Open+Sans:wght@300;400;700&display=swap">
<style>
  :root {
    --backdrop: #e4e5e6;
    --card-white: #ffffff;
    --card-grey: #666a6b;
    --teal-blue: #1f6e9c;
    --text-grey: #6a6d70;
    --rule-grey: #55585a;
    --wordmark-light: #f2f3f3;
  }
  * { margin: 0; padding: 0; box-sizing: border-box; }
  html, body {
    width: 1200px; height: 900px; overflow: hidden;
    background: var(--backdrop);
    font-family: "Open Sans", Arial, sans-serif;
  }
  .canvas { position: relative; width: 1200px; height: 900px; }
  .card {
    position: absolute; left: 250px; width: 700px; height: 400px;
    box-shadow: 0 6px 18px rgba(0,0,0,0.18);
  }
  .card--front { top: 30px; background: var(--card-white); }
  .card--back { top: 470px; background: var(--card-grey); }

  .wordmark {
    position: absolute; font-weight: 300; letter-spacing: 1px; line-height: 1;
    white-space: nowrap;
  }
  .card--front .wordmark {
    right: 48px; top: 70px; font-size: 48px; color: var(--teal-blue);
  }
  .card--back .wordmark {
    right: 40px; bottom: 48px; font-size: 44px; color: var(--wordmark-light);
  }

  .person { position: absolute; left: 40px; top: 148px; }
  .person__name {
    font-size: 23px; font-weight: 700; color: var(--teal-blue); line-height: 1.1;
  }
  .person__title { font-size: 15px; color: var(--text-grey); margin-top: 2px; }
  .divider {
    position: absolute; left: 40px; top: 178px; width: 590px; height: 1.5px;
    background: var(--rule-grey);
  }

  .contact-list {
    position: absolute; left: 40px; top: 236px; list-style: none;
    font-size: 15px; color: var(--text-grey); line-height: 22px;
  }
  .contact-list li { display: flex; align-items: center; gap: 10px; white-space: nowrap; }
  .contact-list svg { width: 13px; height: 13px; flex: none; }

  .company {
    position: absolute; right: 70px; top: 262px; text-align: right;
    font-size: 15px; font-style: normal; color: var(--text-grey); line-height: 21px;
    white-space: nowrap;
  }
  .company__name { font-weight: 700; color: var(--teal-blue); }
</style>
</head>
<body>
<main class="canvas">
  <section class="card card--front" aria-label="Business card front">
    <div class="wordmark">QuietHarbour</div>

    <div class="person">
      <div class="person__name">Marta Holloway</div>
      <div class="person__title">Director</div>
    </div>
    <div class="divider"></div>

    <ul class="contact-list">
      <li>
        <svg viewBox="0 0 16 16" aria-hidden="true"><path fill="#1f6e9c" d="M2 5c0-2 2-3 6-3s6 1 6 3l-1 1.5-2.5-.5V4.5h-5V6L3 6.5zM4 8h8l1.5 6h-11z"/><circle cx="8" cy="10.5" r="1.6" fill="#fff"/></svg>
        +61 498203617
      </li>
      <li>
        <svg viewBox="0 0 16 16" aria-hidden="true"><rect x="1.5" y="3.5" width="13" height="9" fill="none" stroke="#1f6e9c" stroke-width="1.3"/><path d="M1.5 3.5 8 9l6.5-5.5" fill="none" stroke="#1f6e9c" stroke-width="1.3"/></svg>
        marta@quietharbour-example.com.au
      </li>
      <li>
        <svg viewBox="0 0 16 16" aria-hidden="true"><circle cx="8" cy="8" r="6.5" fill="#1f6e9c"/><path d="M1.5 8h13M8 1.5v13M3 4.5h10M3 11.5h10" stroke="#fff" stroke-width="0.9"/><ellipse cx="8" cy="8" rx="3" ry="6.5" fill="none" stroke="#fff" stroke-width="0.9"/></svg>
        www.quietharbour-example.com.au
      </li>
    </ul>

    <address class="company">
      <div class="company__name">Quiet Harbour Pty Ltd</div>
      <div>Tourism Marketing &amp; Representation</div>
      <div>87 Wendover Parade</div>
      <div>Fernleigh, Westvale, 3999 Australia</div>
    </address>
  </section>

  <section class="card card--back" aria-label="Business card back">
    <div class="wordmark">QuietHarbour</div>
  </section>
</main>
</body>
</html>
```